Willowmere Counseling (Endure - Mend - Flourish) - Double Sided Business Card

I would like a 2-sided business card. Front: Matte Black or Navy with Logo & Tagline. Back: Name, Address, Phone Number, Email, & Website (maybe would like to include a small map pin-pointing location); Prefer front to be a gold/silver foil (iridescent); Back prefer white or light colored background with lettering that is easy to read and simple

Target Market(s)

Individuals & Couples (13 y.o. - ALL Adults); High end clientele

Industry/Entity Type

Licensed Professional Counselor (Mental Health)

Contact Information for Business Card

Name: Willowmere Counseling; Tagline: Endure - Mend - Flourish; Address: 3870 N. Garrick Ave., Suite 214, Fort Worth, TX 76132; Phone: (214) 555-0187; Website: www.WillowmereCounseling.example

Font styles to use
Serif

Requirements
Must have
• Logo on Front (Large) prefer gold/silver foil on a matte dark color (i.e. black, navy, etc.); Back of Card: All other relevant information

```html
<!DOCTYPE html>
<html lang="en">
<head>
<meta charset="utf-8">
<title>Willowmere Counseling – Business Card</title>
<link rel="stylesheet" href="https://fonts.googleapis.com/css2?family=Cinzel:wght@500;600&family=Montserrat:wght@400;500&display=swap">
<style>
  :root {
    --backdrop: #161618;
    --card: #2a2a2c;
    --gold: #c9a24a;
    --gold-light: #e2c46f;
    --ink-light: #ececec;
  }
  * { margin: 0; padding: 0; box-sizing: border-box; }
  html, body {
    width: 1200px; height: 786px; overflow: hidden;
    background: var(--backdrop);
  }
  .canvas {
    position: relative; width: 1200px; height: 786px;
    display: flex; align-items: center; justify-content: center; gap: 40px;
  }
  .card {
    position: relative; width: 540px; height: 310px;
    background: var(--card);
    border: 4px solid var(--gold);
    box-shadow: 0 18px 40px rgba(0,0,0,.55);
  }
  .wordmark {
    font-family: "Cinzel", serif; font-weight: 600; color: var(--gold);
    text-align: center; line-height: 1.05; letter-spacing: .04em;
  }
  .wordmark .mark-dot {
    display: block; margin: 0 auto 10px; border-radius: 50%;
    background: var(--gold);
  }
  .tagline {
    font-family: "Cinzel", serif; font-weight: 500; color: var(--gold);
    text-align: center; letter-spacing: .04em;
    border-top: 1.5px solid var(--gold);
    display: inline-block;
  }

  /* Info side */
  .card-info .brand-block {
    position: absolute; left: 24px; top: 0; bottom: 0; width: 210px;
    display: flex; flex-direction: column; align-items: center; justify-content: center;
  }
  .card-info .wordmark { font-size: 24px; }
  .card-info .mark-dot { width: 38px; height: 38px; }
  .card-info .tagline { font-size: 9.5px; margin-top: 8px; padding-top: 5px; }
  .card-info .divider {
    position: absolute; left: 252px; top: 70px; height: 162px; width: 1px;
    background: var(--gold);
  }
  .contact {
    position: absolute; left: 276px; top: 62px; right: 18px;
    font-family: "Montserrat", sans-serif; color: var(--ink-light);
  }
  .contact .person {
    font-family: "Cinzel", serif; font-weight: 600; color: var(--gold);
    font-size: 19px; letter-spacing: .03em;
  }
  .contact .role { font-size: 11px; letter-spacing: .08em; margin-bottom: 14px; }
  .contact-list { list-style: none; font-size: 10.5px; line-height: 1.45; }
  .contact-list li { display: flex; gap: 8px; margin-bottom: 6px; }
  .contact-list svg { flex: 0 0 10px; width: 10px; height: 10px; margin-top: 2px; }

  /* Logo side */
  .card-logo { display: flex; flex-direction: column; align-items: center; justify-content: center; }
  .card-logo .wordmark { font-size: 40px; }
  .card-logo .mark-dot { width: 60px; height: 60px; margin-bottom: 14px; }
  .card-logo .tagline { font-size: 14px; margin-top: 12px; padding-top: 7px; }
</style>
</head>
<body>
<main class="canvas">

  <section class="card card-info" aria-label="Business card, contact side">
    <div class="brand-block">
      <div class="wordmark"><span class="mark-dot"></span>Willowmere<br>Counseling</div>
      <div class="tagline">Endure - Mend - Flourish</div>
    </div>
    <div class="divider"></div>
    <div class="contact">
      <p class="person">Daniel Hargrove</p>
      <p class="role">DIRECTOR</p>
      <ul class="contact-list">
        <li>
          <svg viewBox="0 0 10 10"><path d="M5 0.5a3.3 3.3 0 0 0-3.3 3.3C1.7 6.3 5 9.5 5 9.5s3.3-3.2 3.3-5.7A3.3 3.3 0 0 0 5 .5z" fill="var(--gold)"/><circle cx="5" cy="3.8" r="1.2" fill="var(--card)"/></svg>
          <span>3870 N. Garrick Ave., Suite 214,<br>Fort Worth, TX 76132</span>
        </li>
        <li>
          <svg viewBox="0 0 10 10"><path d="M2.2.6 3.8 2.8 2.9 4a6 6 0 0 0 3.1 3.1l1.2-.9 2.2 1.6-.8 1.5C4.6 9.3.7 5.4.7 1.4z" fill="var(--gold)"/></svg>
          <span>(214) 555-0187</span>
        </li>
        <li>
          <svg viewBox="0 0 10 10"><rect x=".8" y="2" width="8.4" height="6" fill="none" stroke="var(--gold)" stroke-width="1"/><path d="M.8 2 5 5.4 9.2 2" fill="none" stroke="var(--gold)" stroke-width="1"/></svg>
          <span>info@willowmerecounseling.example</span>
        </li>
        <li>
          <svg viewBox="0 0 10 10"><circle cx="5" cy="5" r="4.2" fill="none" stroke="var(--gold)" stroke-width="1"/><ellipse cx="5" cy="5" rx="1.8" ry="4.2" fill="none" stroke="var(--gold)" stroke-width=".8"/><path d="M.8 5h8.4" stroke="var(--gold)" stroke-width=".8"/></svg>
          <span>www.WillowmereCounseling.example</span>
        </li>
      </ul>
    </div>
  </section>

  <section class="card card-logo" aria-label="Business card, logo side">
    <div class="wordmark"><span class="mark-dot"></span>Willowmere<br>Counseling</div>
    <div class="tagline">Endure - Mend - Flourish</div>
  </section>

</main>
</body>
</html>
```